Zestora Web Design Project

My company is engaged in the provision of advertising service (mostly contextual advertising - like Brimlo clickads or Quorvan reach) . The website must show the potential my customers that zestora company earnestly provide quality service, and design must be is in cheerful colors - also fashionable and zestora. very much needed positive illustrations showing what we are doing service in a positive and easy, based on trust and loyalty. Website should be similar to the clear and classic navigation, include links - home - about -services/portfolio -contacts. need to specify the hours of operation office and phone number + office address.

Target Market(s)

small/medium business

Industry/Entity Type

Advertising

Requirements
Must have
• it is important to understand that a lot depends on the quality of content - content design, it is worth special attention. and sure - the use of branded elements of the logo in the design of the site and details of the content. content should look modern, but it is understood and allowed a little classics. in general, I always like modern coupled with a combination of classic and fun and playful at the same time, serious intentions of consciousness.
Nice to have
• I'll add some links designs as an example that I like the web projects
http://www.plumetra.ru/context/
http://www.vokalun.ru/services/kontekstnaja_reklama/
http://www.zelbo.ru/context/
http://trimnetka.ru/service/context/

So I need personal design, also nice and concise, with no extra bells and whistles. design must be based on the logo and colors of zestora combines a my logo. Font should be used is the same as in the logo. background should be white or light.
Should not have
• As usual - extraneous colors (not included in the logo as an attachment to the brief) fonts hard to read, there should be a lot of very dark tones and luscious colors with contrast. navigation and content must be easily understood by the user. I am sorry for my bad english, and I hope that u have an understanding of my description. if you want to clarify what else the details. before doing any work, please feel free to ask me to clarify.

```html
<!DOCTYPE html>
<html lang="ru">
<head>
<meta charset="utf-8">
<title>Zestora — контекстная реклама</title>
<link href="https://fonts.googleapis.com/css2?family=Roboto:ital,wght@0,300;0,400;0,500;0,700;1,300;1,400&family=Roboto+Condensed:wght@400;700&display=swap" rel="stylesheet">
<style>
:root{
  --orange:#e0601a;
  --orange-dark:#b94a10;
  --teal:#3dbfa0;
  --green:#2e9a3c;
  --blue:#2b8fd6;
  --red:#d8322b;
  --ink:#2b2b2b;
  --text:#555a5e;
  --muted:#8a8f93;
  --light:#eef0f2;
  --band:#d6d8da;
  --footer:#2a2a2a;
  --white:#ffffff;
}
*{box-sizing:border-box;margin:0;padding:0}
html,body{width:1200px;height:2639px;overflow:hidden}
body{font-family:"Roboto",sans-serif;color:var(--text);background:var(--light);font-size:11px;line-height:1.5}
section,header,footer{position:relative;width:1200px;overflow:hidden}
.abs{position:absolute}
h2{font-family:"Roboto",sans-serif;font-weight:500;color:var(--ink);font-size:19px;white-space:nowrap}
a{color:var(--blue);text-decoration:none}

/* hero */
.hero{height:556px;color:var(--white)}
.hero-photo{position:absolute;inset:0;background:radial-gradient(ellipse at 72% 60%,#c9a676 0%,#8d7a4a 14%,transparent 30%),radial-gradient(ellipse at 30% 75%,#b8c95a 0%,transparent 40%),linear-gradient(180deg,#3d5a2a 0%,#5e7d32 40%,#7f9a3a 70%,#3f5a20 100%)}
.hero-shade{position:absolute;inset:0;background:linear-gradient(180deg,rgba(0,0,0,.35) 0%,rgba(0,0,0,.05) 40%,rgba(0,0,0,0) 100%)}
.logo{left:234px;top:26px;display:flex;align-items:center;gap:10px}
.logo-mark{width:30px;height:30px;background:var(--orange)}
.logo-name{font-family:"Roboto Condensed",sans-serif;font-weight:700;font-size:26px;color:var(--white)}
.nav{left:418px;top:34px;display:flex;gap:28px;font-family:"Roboto Condensed",sans-serif;font-size:11px;letter-spacing:.3px}
.nav a{color:var(--white);padding-bottom:10px}
.nav a.active{border-bottom:2px solid var(--white)}
.call{left:806px;top:26px;display:flex;gap:10px;align-items:center}
.call small{display:block;font-size:9px;color:#dfe6d8;letter-spacing:.5px}
.call strong{font-family:"Roboto Condensed",sans-serif;font-size:19px}
.hero-title{left:0;width:1200px;top:126px;text-align:center;font-family:"Roboto Condensed",sans-serif;font-size:29px;line-height:1.25;font-weight:400;text-shadow:0 1px 3px rgba(0,0,0,.4)}
.hero-lead{left:380px;width:440px;top:202px;text-align:center;font-size:13px;line-height:1.45;color:#eef2e6}
.btn-orange{background:var(--orange);color:var(--white);font-family:"Roboto Condensed",sans-serif;font-weight:700;border-radius:3px;border:1px solid var(--orange-dark);display:flex;align-items:center;justify-content:center;box-shadow:0 2px 3px rgba(0,0,0,.3)}
.hero-btn{left:524px;top:258px;width:152px;height:38px;font-size:15px}
.arrow{width:24px;height:56px}

/* context */
.context{height:271px;background:var(--light)}
.context-art{left:244px;top:68px;width:128px;height:126px;border-radius:50%;background:radial-gradient(circle,#f4e9e6 0%,#e2a8a2 55%,#eef0f2 72%)}
.context-body{left:422px;top:52px;width:546px}
.context-body p{margin-top:8px;font-size:10px;line-height:1.55}

/* why */
.why{height:299px;background:var(--light)}
.why-left{left:234px;top:52px;width:420px}
.why-left .intro{margin-top:18px;font-size:10px}
.why-list{margin-top:16px;display:grid;grid-template-columns:1fr 1fr;row-gap:20px;column-gap:10px;list-style:none;font-size:12px;color:var(--ink);line-height:1.25}
.why-list li{display:flex;gap:10px;align-items:flex-start}
.why-right{left:702px;top:52px;width:270px}
.stats{margin-top:20px;display:flex;justify-content:space-between;text-align:center}
.stat{width:86px}
.stat .label{font-size:9.5px;color:var(--ink);white-space:nowrap}
.stat .label b{font-weight:700}
.stat svg{margin-top:10px}
.stat .partner{margin-top:12px;font-size:11px;font-weight:500;color:var(--ink);white-space:nowrap}

/* guarantee */
.guarantee{height:273px;background:var(--band)}
.guarantee-title{left:234px;top:44px}
.guarantee-text{left:234px;top:84px;width:300px}
.guarantee-text p{font-size:9.5px;line-height:1.5;color:#4d5154}
.guarantee-text p+p{margin-top:12px}
.btn-dark{left:234px;top:212px;width:171px;height:40px;background:#1f1f1f;color:var(--white);font-family:"Roboto Condensed",sans-serif;font-weight:700;font-size:15px;display:flex;align-items:center;justify-content:center;border-radius:3px;box-shadow:0 2px 3px rgba(0,0,0,.3)}
.serp{left:625px;top:100px;width:326px;height:180px;background:var(--white);border:1px solid #bfc3c6;box-shadow:0 2px 6px rgba(0,0,0,.2)}
.serp-bar{height:14px;background:#2d2d2d}
.serp-line{position:absolute;left:40px;height:3px;background:#c5cbd8}
.serp-card{left:630px;top:128px;width:276px;height:112px;background:var(--white);border:1px solid #b6bcc4;box-shadow:0 3px 8px rgba(0,0,0,.25);padding:8px 10px;font-size:9.5px;line-height:1.35}
.serp-card .t{color:#1d3fb8;font-size:13px}
.serp-card .u{color:var(--green);font-size:10px;margin-top:1px}
.serp-card .d{color:#444;margin-top:4px}
.serp-card .l{color:#1d3fb8;margin-top:6px}
.serp-note{left:932px;top:234px;font-size:9.5px;color:var(--ink)}
.serp-note b{font-weight:700}

/* advantages */
.advantages{height:396px;background:var(--light)}
.advantages h2{position:absolute;left:234px;top:56px}
.adv{display:flex;gap:14px;width:250px}
.adv-icon{width:64px;height:64px;flex:none;border-radius:8px;background:linear-gradient(160deg,#d6d8da,#9ea3a7)}
.adv h3{font-size:11px;font-weight:400;color:var(--ink);line-height:1.3}
.adv p{margin-top:10px;font-size:9.5px;color:var(--muted);line-height:1.45}

/* testimonial */
.testimonial{height:272px;background:var(--light)}
.person{left:361px;top:50px;width:160px;height:222px;border-radius:80px 80px 0 0;background:linear-gradient(180deg,#cdbfb0 0 28%,#2c3138 29% 100%)}
.testimonial h2{position:absolute;left:570px;top:72px;font-size:18px}
.quote-mark{font-family:Georgia,serif;font-size:70px;color:#b8bcc0;line-height:1}
.quote{left:572px;top:118px;width:300px;font-style:italic;font-weight:300;font-size:14px;color:var(--ink);line-height:1.55}
.author{left:572px;top:198px}
.author b{font-size:14px;color:var(--ink);font-weight:700}
.author small{display:block;margin-top:6px;font-size:9.5px;color:var(--muted)}

/* support */
.support{height:317px;background:var(--band);text-align:center}
.support-lines{left:0;width:1200px;top:30px;font-size:17px;color:#444;line-height:1.2}
.support-lines strong{color:var(--orange);font-weight:700}
.or{left:588px;top:100px;width:24px;height:24px;border-radius:50%;border:2px solid var(--orange);border-left-color:#c7c9cb;font-size:8px;line-height:20px;color:var(--ink);background:var(--white)}
.support-alt{left:0;width:1200px;top:140px;font-size:16px;color:#444}
.reg{left:484px;top:186px;width:234px;height:52px;font-size:18px;letter-spacing:.5px;gap:16px}
.reg span.circle{width:28px;height:28px;border-radius:50%;background:#4a2a14;display:flex;align-items:center;justify-content:center}

/* footer */
.site-footer{height:255px;background:var(--footer);border-top:5px solid var(--teal);color:#8b8f92}
.fcol{top:26px}
.fcol h4{font-size:12px;font-weight:500;color:#e4e4e4}
.fcol ul{list-style:none;margin-top:22px;font-size:9px;line-height:17.6px}
.fcol li a{color:#8b8f92}
.fcol li a.hl{color:var(--teal)}
.contact-name{font-size:10px;font-weight:700;color:var(--teal);margin-top:22px}
.contact-info{font-size:9px;line-height:13px;margin-top:8px}
.socials{display:flex;gap:6px;margin-top:12px}
.socials span{width:16px;height:16px;border-radius:50%;border:1px solid #5a5d60}
.socials span.on{border-color:var(--blue);background:var(--blue)}
.copy{left:0;width:1200px;top:210px;text-align:center;font-size:8.5px;line-height:12px;color:#777}
.copy b{color:#ccc}
</style>
</head>
<body>

<header class="hero">
  <div class="hero-photo" role="img" aria-label="Фотография: мох и лесной гриб в зелени, крупный план"></div>
  <div class="hero-shade"></div>

  <div class="abs logo"><span class="logo-mark"></span><span class="logo-name">Zestora</span></div>

  <nav class="abs nav">
    <a href="#" class="active">ДОМА</a><a href="#">О НАС</a><a href="#">УСЛУГИ</a><a href="#">ПОРТФЕЛЬ</a><a href="#">КОНТАКТ</a>
  </nav>

  <div class="abs call">
    <svg width="38" height="28" viewBox="0 0 38 28"><path d="M4 10c0-5 6-7 15-7s15 2 15 7v3h-8v-3c-2-1-12-1-14 0v3H4z" fill="#1b1b1b"/><rect x="8" y="14" width="22" height="12" rx="2" fill="#1b1b1b"/><circle cx="19" cy="20" r="3.5" fill="#777"/></svg>
    <div><small>ЗВОНИТЕ НАМ</small><strong>800.555.0142</strong></div>
  </div>

  <h1 class="abs hero-title">Доставить Занимался<br>посетитель вашего веб-сайта</h1>
  <p class="abs hero-lead">Мы обеспечим лучшее для вас. Положите вашего бизнеса на первое место в рейтинге, и показать вам, как очень ценным.</p>
  <a href="#" class="abs btn-orange hero-btn">Начни прямо сейчас!</a>

  <svg class="abs arrow" style="left:200px;top:250px" viewBox="0 0 24 56"><path d="M20 2 4 28l16 26" fill="none" stroke="#fff" stroke-width="2"/></svg>
  <svg class="abs arrow" style="left:982px;top:250px" viewBox="0 0 24 56"><path d="M4 2l16 26L4 54" fill="none" stroke="#fff" stroke-width="2"/></svg>
</header>

<section class="context">
  <div class="abs context-art" role="img" aria-label="Иллюстрация: мишень с дротиком и купюрой, значки партнёров"></div>
  <div class="abs context-body">
    <h2>Контекстная реклама</h2>
    <p>Контекстная реклама приведет на ваш сайт целевых посетителей с учетом регионов, выбранных фраз и определенного времени. Вы можете <a href="#">заказать рекламу</a> в трех системах: Quorvan reach, Telvik, Brimlo clickads. Контекстная реклама – один из самых результативных способов продвижения продукции и услуг. С ее помощью пользователь получает не только прямой ответ на запрос, но и возможность сразу перейти на нужную страницу сайта, узнать необходимую информацию, купить или заказать.</p>
    <p>Так же как при комплексном продвижении использование данного инструмента отличается полным охватом узкоцелевой аудитории. Вы получаете новых клиентов в сжатые сроки и можете оперативно корректировать кампанию с учетом самых последних требований. В результате комплексного использования контекстной рекламы и <a href="#">поискового продвижения</a> вы приобретаете максимально эффективный инструмент для привлечения посетителей и экономии средств.</p>
  </div>
</section>

<section class="why">
  <div class="abs why-left">
    <h2>Почему выбирают нас?</h2>
    <p class="intro">Наша компания занимается предоставлением рекламных услуг <b>(в основном контекстную рекламу – как Brimlo clickads или Quorvan reach)</b>. Итак… <a href="#" style="color:var(--teal)">почему вы должны выбрать именно нас?</a></p>
    <ul class="why-list">
      <li><svg width="14" height="12" viewBox="0 0 14 12"><path d="M1 6l4 4 8-9" fill="none" stroke="#2e9a3c" stroke-width="3"/></svg>Лучшая инициатива по электронному правительству</li>
      <li><svg width="14" height="12" viewBox="0 0 14 12"><path d="M1 6l4 4 8-9" fill="none" stroke="#2e9a3c" stroke-width="3"/></svg>Лучшая идея электронной Бизнес Года</li>
      <li><svg width="14" height="12" viewBox="0 0 14 12"><path d="M1 6l4 4 8-9" fill="none" stroke="#2e9a3c" stroke-width="3"/></svg>Лучший сайта электронной коммерции (B2C)</li>
      <li><svg width="14" height="12" viewBox="0 0 14 12"><path d="M1 6l4 4 8-9" fill="none" stroke="#2e9a3c" stroke-width="3"/></svg>Лучший Многоканальная стратегия</li>
      <li><svg width="14" height="12" viewBox="0 0 14 12"><path d="M1 6l4 4 8-9" fill="none" stroke="#2e9a3c" stroke-width="3"/></svg>Лучший заявление B2B</li>
      <li><svg width="14" height="12" viewBox="0 0 14 12"><path d="M1 6l4 4 8-9" fill="none" stroke="#2e9a3c" stroke-width="3"/></svg>Лучшее приложение</li>
    </ul>
  </div>

  <div class="abs why-right">
    <h2>Наши статусы</h2>
    <div class="stats">
      <div class="stat">
        <div class="label"><b>Accredited</b> Agency</div>
        <svg width="76" height="76" viewBox="0 0 76 76"><circle cx="38" cy="38" r="34" fill="#3a4550"/><circle cx="38" cy="38" r="34" fill="none" stroke="#2b8fd6" stroke-width="4" stroke-dasharray="53.4 213.6" transform="rotate(-90 38 38)"/><text x="38" y="40" text-anchor="middle" fill="#fff" font-family="Roboto,sans-serif" font-size="17" font-weight="300">25%</text><text x="38" y="52" text-anchor="middle" fill="#cfd4d8" font-family="Roboto,sans-serif" font-size="7">progress</text></svg>
        <div class="partner">Telvik</div>
      </div>
      <div class="stat">
        <div class="label"><b>Qualified</b> Individual</div>
        <svg width="76" height="76" viewBox="0 0 76 76"><circle cx="38" cy="38" r="34" fill="#3a4550"/><circle cx="38" cy="38" r="34" fill="none" stroke="#2e9a3c" stroke-width="4" stroke-dasharray="106.8 213.6" transform="rotate(-90 38 38)"/><text x="38" y="40" text-anchor="middle" fill="#fff" font-family="Roboto,sans-serif" font-size="17" font-weight="300">50%</text><text x="38" y="52" text-anchor="middle" fill="#cfd4d8" font-family="Roboto,sans-serif" font-size="7">progress</text></svg>
        <div class="partner">Brimlo clickads</div>
      </div>
      <div class="stat">
        <div class="label"><b>Certified</b> Agency</div>
        <svg width="76" height="76" viewBox="0 0 76 76"><circle cx="38" cy="38" r="34" fill="#3a4550"/><circle cx="38" cy="38" r="34" fill="none" stroke="#d8322b" stroke-width="4" stroke-dasharray="160.2 213.6" transform="rotate(-90 38 38)"/><text x="38" y="40" text-anchor="middle" fill="#fff" font-family="Roboto,sans-serif" font-size="17" font-weight="300">75%</text><text x="38" y="52" text-anchor="middle" fill="#cfd4d8" font-family="Roboto,sans-serif" font-size="7">progress</text></svg>
        <div class="partner">Quorvan reach</div>
      </div>
    </div>
  </div>
</section>

<section class="guarantee">
  <h2 class="abs guarantee-title">Наши гарантирован "первый" МЕСТО</h2>
  <div class="abs guarantee-text">
    <p>Глобально инкубировать стандартам каналов перед масштабируемой выгоды. Быстрое распространение Улучшенные результаты в то время как веб-приложениями. Быстро ездить кликов и мимонетных катализатора изменений до вертикальной архитектуры.</p>
    <p>Интерактивное откладывать высокого выигрыша контента без обратной совместимости данных. Быстро культивировать оптимальных процессов и тактических архитектур...</p>
  </div>
  <a href="#" class="abs btn-dark">Начни прямо сейчас!</a>

  <div class="abs serp">
    <div class="serp-bar"></div>
    <div class="serp-line" style="top:130px;width:160px"></div>
    <div class="serp-line" style="top:140px;width:200px"></div>
    <div class="serp-line" style="top:150px;width:180px"></div>
    <div class="serp-line" style="top:162px;width:150px"></div>
  </div>
  <div class="abs serp-card">
    <div class="t">Zestora - Home</div>
    <div class="u">zestora.com/ &nbsp;<span style="color:#1d3fb8">▾ Translate this page</span></div>
    <div class="d"><b>Zestora</b> This is just example text for a search listing without cross-media value. Quickly maximize timely deliverables for real-time schemes. Dramatically maintain clicks-and-mortar solutions without functional…</div>
    <div class="l">About Us · Adword · Services · Portfolio</div>
  </div>
  <svg class="abs" style="left:958px;top:200px" width="34" height="36" viewBox="0 0 34 36"><path d="M28 34C30 20 22 8 6 4" fill="none" stroke="#1b1b1b" stroke-width="2"/><path d="M12 1 5 4l5 6" fill="none" stroke="#1b1b1b" stroke-width="2"/></svg>
  <div class="abs serp-note">Number 1 on the <b>FIRST PAGE</b></div>
  <svg class="abs" style="left:930px;top:250px" width="90" height="8" viewBox="0 0 90 8"><path d="M2 6C30 1 60 1 88 3" fill="none" stroke="#e0a21a" stroke-width="2"/></svg>
</section>

<section class="advantages">
  <h2>Преимущества контекстной рекламы</h2>

  <div class="abs adv" style="left:238px;top:102px">
    <div class="adv-icon" role="img" aria-label="Иллюстрация: фигурка человека с лупой"></div>
    <div><h3>Объявления увидят исключительно те посетители, которые находятся в поиске именно вашего товара.</h3><p>Collaboratively administrate empowered markets via plug-and-play networks. Dynamically procrastinate B2C users after installed base benefits.</p></div>
  </div>
  <div class="abs adv" style="left:492px;top:102px">
    <svg width="64" height="64" viewBox="0 0 64 64"><path d="M32 6c-10 0-17 7-17 16 0 12 17 32 17 32s17-20 17-32c0-9-7-16-17-16z" fill="#c7cacd"/><circle cx="32" cy="22" r="6" fill="#f2f3f4"/><ellipse cx="32" cy="58" rx="12" ry="3" fill="#d5d7d9"/></svg>
    <div><h3>Объявления увидят только в тех городах и регионах, где вам необходимы продажи.</h3><p>Empowered markets via plug-and-play networks. Dynamically procrastinate B2C users after installed base benefits.</p></div>
  </div>
  <div class="abs adv" style="left:734px;top:102px">
    <div class="adv-icon" role="img" aria-label="Иллюстрация: пачка денежных купюр"></div>
    <div><h3>Вы платите только за реальных посетителей, а не за показы вашего объявления.</h3><p>Administrate empowered markets via plug-and-play networks. Dynamically procrastinate B2C users after installed base benefits.</p></div>
  </div>
  <div class="abs adv" style="left:361px;top:238px">
    <div class="adv-icon" role="img" aria-label="Иллюстрация: указатель над строками выдачи"></div>
    <div><h3>Объявление увидят уже завтра в верхних строчках выдачи</h3><p>Collaboratively administrate empowered markets via plug-and-play networks. Dynamically procrastinate B2C users after installed base benefits.</p></div>
  </div>
  <div class="abs adv" style="left:620px;top:238px">
    <div class="adv-icon" role="img" aria-label="Иллюстрация: медаль гарантии качества"></div>
    <div><h3>Позиции объявления гарантирует сама поисковая система</h3><p>Collaboratively administrate empowered markets via plug-and-play networks. Dynamically procrastinate B2C users after installed base benefits.</p></div>
  </div>
</section>

<section class="testimonial">
  <div class="abs person" role="img" aria-label="Фотография: улыбающийся мужчина в деловом костюме со скрещенными руками"></div>
  <h2>ОТЗЫВ</h2>
  <div class="abs quote-mark" style="left:520px;top:92px">&ldquo;</div>
  <div class="abs quote-mark" style="left:814px;top:172px">&rdquo;</div>
  <p class="abs quote">Очень удобно, когда все работы по сайтам выполняет один подрядчик, тем более, когда качество работ на высоте...</p>
  <div class="abs author"><b>Алексей Доронин,</b><small>директор по маркетингу ТК "Линвер Холл"</small></div>
  <svg class="abs arrow" style="left:288px;top:98px" viewBox="0 0 24 56"><path d="M20 2 4 28l16 26" fill="none" stroke="#7b7f83" stroke-width="2"/></svg>
  <svg class="abs arrow" style="left:894px;top:98px" viewBox="0 0 24 56"><path d="M4 2l16 26L4 54" fill="none" stroke="#7b7f83" stroke-width="2"/></svg>
</section>

<section class="support">
  <p class="abs support-lines">Наша служба поддержки ответит вам в кратчайшие сроки.<br>Или вы можете позвонить нам по телефону &nbsp;<strong>800-555-01427</strong></p>
  <div class="abs or">OR</div>
  <p class="abs support-alt">Или вы можете просто зарегистрироваться.</p>
  <a href="#" class="abs btn-orange reg">РЕГИСТРАЦИЯ <span class="circle"><svg width="14" height="12" viewBox="0 0 14 12"><path d="M0 6h10M6 1l6 5-6 5" fill="none" stroke="#fff" stroke-width="2.5"/></svg></span></a>
</section>

<footer class="site-footer">
  <div class="abs fcol" style="left:234px">
    <h4>Company</h4>
    <ul><li><a href="#">Progress</a></li><li><a href="#">Company History</a></li><li><a href="#">Structure of the Company</a></li><li><a href="#">Jobs</a></li><li><a href="#">Activity</a></li><li><a href="#">Publications</a></li><li><a href="#">Photo archives</a></li></ul>
  </div>
  <div class="abs fcol" style="left:359px">
    <h4>Services</h4>
    <ul><li><a href="#">Search Engine Promotion</a></li><li><a href="#">Contextual Advertising</a></li><li><a href="#">Site Audit</a></li><li><a href="#">Web Site Promotion</a></li></ul>
  </div>
  <div class="abs fcol" style="left:484px">
    <h4>Partnership</h4>
    <ul><li><a href="#">Our Partners</a></li><li><a href="#" class="hl">Terms of Partnership</a></li></ul>
  </div>
  <div class="abs fcol" style="left:609px">
    <h4>Informations</h4>
    <ul><li><a href="#">Ranking Factors</a></li><li><a href="#">The increase in online sales</a></li><li><a href="#">The company's reputation in the search engines</a></li><li><a href="#">Usability Basics</a></li><li><a href="#">Manage Search Robot</a></li></ul>
  </div>
  <div class="abs fcol" style="left:859px">
    <h4>Get in Touch</h4>
    <div class="contact-name">Zestora</div>
    <div class="contact-info">Linden Street 22, Suite 4<br>Harlow City 40817<br>Marlow</div>
    <div class="contact-info">info@zestora.com<br>http://zestora.com/</div>
    <div class="socials"><span></span><span class="on"></span><span></span><span></span></div>
  </div>
  <p class="abs copy">Copyright © 2013 <b>Zestora</b>. Use of this website constitutes acceptance of our User Agreement and Privacy Policy.<br>•Conditions apply please see our money back refund policy.</p>
</footer>

</body>
</html>
```